hobby beef jerky maker looking to break into the commercial market

We need product labels designed for each flavour of jerky we make. Currently have 3 flavours that we are ready to share with the world. We need in your face designs to help us stand out from an already crowded market.
The product name is Rivet Beef Jerky.
The flavours we offer have been named Porch Lope, Ember Glaze and Chili Knack.
The Rivet Beef Jerky Title should remain the same across the three labels but the design for each flavour can change as you see fit.
Label needs to fit within 110mm x 110mm to suit our current packaging

Industry/Entity Type

Food Production

Logo Text

Morvendale Apiary

Colors

Designer to choose colors to be used in the design.

Requirements
Must have
• "Rivet Beef Jerky" font and colour must remain the same across the 3 designs
Nice to have
• The labels will be used on the clear side of the packaging with a small space towards the bottom being left visible so the product inside can be seen

```html
<!DOCTYPE html>
<html lang="en">
<head>
<meta charset="utf-8">
<title>Rivet Beef Jerky – Porch Lope Label</title>
<link href="https://fonts.googleapis.com/css2?family=Archivo:wght@800&family=Open+Sans:wght@400;600&display=swap" rel="stylesheet">
<style>
  :root {
    --backdrop: #4b5a5a;
    --label-blue: #4dd5fb;
    --gold: #d4a540;
    --gold-light: #e8c66a;
    --plaque-brown: #221109;
    --tagline-orange: #e8842a;
    --flavour-blue: #52d6f6;
    --badge-red: #6b1a12;
    --white: #ffffff;
  }
  * { margin: 0; padding: 0; box-sizing: border-box; }
  html, body {
    width: 1200px;
    height: 1000px;
    overflow: hidden;
    background: var(--backdrop);
  }
  .canvas {
    position: relative;
    width: 1200px;
    height: 1000px;
  }
  .label {
    position: absolute;
    left: 255px;
    top: 172px;
    width: 690px;
    height: 657px;
  }
  .label-field { fill: var(--label-blue); stroke: var(--gold); stroke-width: 2; }
  .plaque { fill: var(--plaque-brown); stroke: var(--gold); stroke-width: 2; }
  .plaque-outline { fill: none; stroke: var(--gold-light); stroke-width: 1; }
  .brand-name {
    font-family: "Archivo", "Arial Black", sans-serif;
    font-weight: 800;
    fill: var(--gold-light);
    text-anchor: middle;
  }
  .tagline {
    font-family: "Open Sans", sans-serif;
    font-weight: 400;
    font-size: 21px;
    fill: var(--tagline-orange);
    text-anchor: middle;
  }
  .flavour-bar { fill: var(--plaque-brown); stroke: var(--gold); stroke-width: 1.5; }
  .flavour-name {
    font-family: "Open Sans", sans-serif;
    font-weight: 600;
    font-size: 21px;
    fill: var(--flavour-blue);
    text-anchor: middle;
  }
  .weight-tag { fill: var(--flavour-blue); stroke: var(--white); stroke-width: 2; }
  .weight-text {
    font-family: "Open Sans", sans-serif;
    font-weight: 600;
    font-size: 16px;
    fill: var(--white);
    text-anchor: middle;
  }
  .badge-ring { fill: var(--gold); }
  .badge-core { fill: var(--badge-red); }
  .badge-ribbon { fill: var(--badge-red); stroke: var(--gold); stroke-width: 1; }
</style>
</head>
<body>
<main class="canvas">
  <svg class="label" viewBox="0 0 476 453" xmlns="http://www.w3.org/2000/svg" aria-label="Rivet Beef Jerky, Porch Lope flavour label">
    <rect class="label-field" x="1" y="1" width="474" height="451"/>

    <g class="quality-badge">
      <circle class="badge-ring" cx="400" cy="48" r="38"/>
      <circle class="badge-core" cx="400" cy="48" r="32"/>
      <circle cx="400" cy="48" r="27" fill="none" stroke="#d4a540" stroke-width="1"/>
      <path class="badge-ribbon" d="M356 64 L444 64 L440 78 L444 92 L356 92 L360 78 Z"/>
    </g>

    <path class="plaque-outline" transform="translate(230 240) scale(1.04) translate(-230 -240)"
      d="M32 150 Q52 150 52 130 L52 118 Q140 118 160 100 Q230 80 300 100 Q320 118 408 118 L408 130 Q408 150 428 150 L428 330 Q408 330 408 350 L408 362 Q320 362 300 380 Q230 400 160 380 Q140 362 52 362 L52 350 Q52 330 32 330 Z"/>
    <path class="plaque"
      d="M32 150 Q52 150 52 130 L52 118 Q140 118 160 100 Q230 80 300 100 Q320 118 408 118 L408 130 Q408 150 428 150 L428 330 Q408 330 408 350 L408 362 Q320 362 300 380 Q230 400 160 380 Q140 362 52 362 L52 350 Q52 330 32 330 Z"/>

    <text class="brand-name" x="230" y="212" font-size="48">RIVET</text>
    <text class="brand-name" x="230" y="266" font-size="40">BEEF JERKY</text>
    <text class="tagline" x="230" y="316">THE TRUE TASTE</text>

    <rect class="flavour-bar" x="22" y="390" width="344" height="44" rx="8"/>
    <text class="flavour-name" x="194" y="420">PORCH LOPE FLAVOUR</text>

    <path class="weight-tag" d="M378 398 Q378 390 386 390 L426 390 Q438 390 438 402 L438 426 Q438 434 430 434 L386 434 Q378 434 378 426 Z"/>
    <text class="weight-text" x="408" y="418">00 g</text>
  </svg>
</main>
</body>
</html>
```